Thimble Deli Needs a Web Page!

Thimble Deli is a gourmet sandwich shop in Baltimore, MD USA.
We are due to open in about a month or so and we need a great web page that looks cool and is easy to use. Our Concept supports local farmers, ranchers, fishmongers & purveyors. All of our menu items are made from scratch using fresh local ingredients.

Target Market(s)

Urban people on the go & Anyone who is hungry and likes a great sandwich

Industry/Entity Type

Shop

Requirements
Must have
• We must have these 8 tabs:
Home
Menus
Gallery
About Us
Media & Events
Hours & Location
Order Online
Contact Us

Also we would like our Logo to be a focal point
Our Color scheme is Red, Black, Grey, White and a reddish-orange
however any and all colors are great and will be considered
We would love an area on the page for our own food photos to be added.
Nice to have
• Baltimore Skyline
Order Online Now Button
Free Wi-Fi Symbol
Dine-In, Take Out, Delivery,
Business Lunches, Tail Gate Platters, Catering
Should not have
• No Stock images of food or chefs.
(We want to put all of our own food photos up later.)
No Pink.

```html
<!DOCTYPE html>
<html lang="en">
<head>
<meta charset="utf-8">
<title>Thimble Deli</title>
<link rel="stylesheet" href="https://fonts.googleapis.com/css2?family=Arimo:wght@400;700&display=swap">
<style>
:root{
  --ink:#222222;
  --bar:#2b2b2b;
  --nav:#3b1a0c;
  --orange:#f07a1e;
  --orange-deep:#d05a00;
  --red:#d8361a;
  --grey-text:#8a8a8a;
  --body-text:#555555;
  --band:#f2f2f2;
  --white:#ffffff;
}
*{margin:0;padding:0;box-sizing:border-box}
html,body{width:1167px;height:1200px;overflow:hidden;background:var(--white);font-family:"Arimo",Arial,sans-serif}
.page{position:relative;width:1167px;height:1200px;overflow:hidden}
.abs{position:absolute}

.topbar{left:0;top:0;width:1167px;height:46px;background:var(--ink)}
.call{left:803px;top:12px;display:flex;align-items:center;gap:12px;color:var(--white);font-size:16px}

.skyline{left:0;top:46px;width:1167px;height:362px;
  background:linear-gradient(180deg,#6e6e6e 0%,#9a9a9a 30%,#4a4a4a 62%,#2e2e2e 80%,#5a5a5a 100%)}

.logo-box{left:140px;top:46px;width:223px;height:108px;background:var(--ink);border-radius:0 0 8px 8px;
  display:flex;align-items:center;justify-content:center;gap:9px}
.logo-dot{width:20px;height:20px;border-radius:50%;background:var(--red);flex:none}
.logo-name{color:var(--white);font-weight:700;font-size:23px;letter-spacing:.3px;white-space:nowrap}

.nav{left:142px;top:283px;width:884px;height:45px;background:var(--nav);display:flex;align-items:center;padding-left:30px}
.nav a{color:var(--white);text-decoration:none;font-size:16px;margin-right:25px;white-space:nowrap}
.nav a.active{color:var(--orange)}

.slider{left:142px;top:328px;width:884px;height:316px;background:linear-gradient(180deg,#ffffff,#f7f7f7);
  box-shadow:0 6px 10px rgba(0,0,0,.25);border:1px solid #dddddd}
.slide-copy{left:6px;top:52px;width:404px;text-align:center}
.slide-copy h1{font-size:23px;line-height:28px;font-weight:700;color:#111;white-space:nowrap}
.slide-copy .lead{margin:22px auto 0;width:340px;font-size:16px;line-height:23px;color:var(--body-text);white-space:nowrap}
.slide-copy .lead span{color:var(--orange);text-decoration:underline}
.btn-learn{display:inline-block;margin-top:8px;background:var(--nav);color:var(--white);font-size:14px;padding:6px 11px;border-radius:3px}
.food-photo{left:410px;top:54px;width:456px;height:188px;border-radius:50%/40%;
  background:radial-gradient(ellipse at 50% 45%,#cfb48a 0%,#a88a60 50%,#222 78%,#fafafa 82%)}
.dots{left:414px;top:297px;display:flex;gap:5px}
.dots i{width:11px;height:11px;border-radius:50%;background:#111}
.dots i.on{background:var(--orange)}

.services{left:0;top:692px;width:1167px;height:265px;background:var(--band)}
.service{width:260px;height:100px}
.service .icon{left:0;top:7px;width:50px;height:55px;border-radius:8px;
  background:linear-gradient(180deg,#ffffff,#cfcfcf);box-shadow:0 1px 3px rgba(0,0,0,.35)}
.service h3{left:64px;top:0;font-size:16px;font-weight:400;color:#222;text-decoration:underline;white-space:nowrap}
.service p{left:64px;top:22px;width:200px;font-size:13.5px;line-height:20px;color:var(--grey-text);letter-spacing:.3px}
.service .more{color:var(--orange);text-decoration:underline;font-size:13px}

.label{font-size:16px;color:var(--orange);border-bottom:1px dotted #999;padding-bottom:3px;white-space:nowrap}
.menu-col h4{font-size:16px;font-weight:700;color:var(--orange-deep);white-space:nowrap}
.menu-col p{margin-top:8px;font-size:13.5px;line-height:16px;color:var(--grey-text)}
.track{left:141px;top:1095px;width:398px;height:11px;background:#333;border-radius:6px;overflow:hidden}
.track .start{position:absolute;left:0;top:0;width:24px;height:11px;background:#999}
.track .grip{position:absolute;left:214px;top:0;width:24px;height:11px;
  background:repeating-linear-gradient(90deg,#c7901c 0 3px,#333 3px 6px)}
.divider{left:617px;top:991px;width:2px;height:110px;background:linear-gradient(180deg,transparent,#bbb,transparent)}
.contact p{font-size:13px;line-height:16px;color:var(--grey-text)}
.contact .mail{margin-top:14px;font-size:14px;color:#3b1a0c;white-space:nowrap}
.contact .copy{margin-top:4px;font-size:14px;color:#222;white-space:nowrap}
.order-btn{left:866px;top:1008px;width:116px;height:25px;background:linear-gradient(180deg,var(--orange),var(--red));
  color:var(--white);font-weight:700;font-size:16px;text-align:center;line-height:23px;border:1px solid #222;white-space:nowrap}
.world{left:840px;top:1054px;width:170px;height:52px;border-radius:40%/50%;
  background:radial-gradient(ellipse at center,#6f6f6f 0%,#9a9a9a 60%,rgba(255,255,255,0) 72%)}

.footer{left:0;top:1143px;width:1167px;height:57px;background:var(--bar)}
.foot-nav{left:142px;top:22px;display:flex;gap:7px}
.foot-nav a{color:var(--white);font-size:13.5px;text-decoration:none;white-space:nowrap}
.foot-nav a.active{color:var(--orange)}
.social{left:888px;top:10px;display:flex;gap:8px}
.social span{width:29px;height:29px;border-radius:4px;background:linear-gradient(180deg,#ffffff,#bdbdbd)}
</style>
</head>
<body>
<div class="page">
  <div class="abs topbar"></div>
  <div class="abs call">
    <svg width="26" height="30" viewBox="0 0 26 30" aria-hidden="true">
      <g fill="none" stroke="#bbb" stroke-width="2">
        <path d="M8 12a6 6 0 0 1 8-6"/><path d="M4 12a10 10 0 0 1 14-9"/>
      </g>
      <rect x="3" y="18" width="20" height="8" rx="2" fill="#ccc"/>
      <circle cx="18" cy="22" r="1.5" fill="#444"/>
    </svg>
    <span>Call Now! 0012-1-555-0198</span>
  </div>

  <div class="abs skyline" role="img" aria-label="Black and white night photo of the Baltimore skyline"></div>

  <div class="abs logo-box">
    <span class="logo-dot"></span>
    <span class="logo-name">THIMBLE DELI</span>
  </div>

  <nav class="abs nav">
    <a class="active" href="#">Home</a><a href="#">Menus</a><a href="#">Gallery</a><a href="#">About Us</a><a href="#">Media &amp; Events</a><a href="#">Hours &amp; Location</a><a href="#">Order Online</a><a href="#">Contact Us</a>
  </nav>

  <section class="abs slider">
    <div class="abs slide-copy">
      <h1>All of our menu items are made from<br>scratch using local ingredients</h1>
      <p class="lead"><span>THIMBLE DELI Lorem ipsum dolor sit amet,</span><br>consectetur adipisicing elit, sed do<br>eiusmod tempor.Duis aute irure dolor in<br>repre henderit in voluptate velit esse cillum<br>dolore eu fugiat nulla.</p>
      <span class="btn-learn">Learn More</span>
    </div>
    <div class="abs food-photo" role="img" aria-label="Photo of a sandwich platter on a black tray"></div>
    <div class="abs dots"><i class="on"></i><i></i><i></i><i></i></div>
  </section>

  <section class="abs services">
    <div class="abs service" style="left:142px;top:30px">
      <div class="abs icon" role="img" aria-label="Dine-in icon"></div>
      <h3 class="abs">Dine-In</h3>
      <p class="abs">Lorem ipsum dolor sit amet, consectetur adipisicing elit,<br><span class="more">More...</span></p>
    </div>
    <div class="abs service" style="left:459px;top:30px">
      <div class="abs icon" role="img" aria-label="Tail gate platters icon"></div>
      <h3 class="abs">Tail Gate Platters</h3>
      <p class="abs">Lorem ipsum dolor sit amet, consectetur adipisicing elit,<br><span class="more">More...</span></p>
    </div>
    <div class="abs service" style="left:775px;top:30px">
      <div class="abs icon" role="img" aria-label="Take out icon"></div>
      <h3 class="abs">Take Out</h3>
      <p class="abs">Lorem ipsum dolor sit amet, consectetur adipisicing elit,<br><span class="more">More...</span></p>
    </div>
    <div class="abs service" style="left:142px;top:156px">
      <div class="abs icon" role="img" aria-label="Business lunch icon"></div>
      <h3 class="abs">Business Lunch</h3>
      <p class="abs">Lorem ipsum dolor sit amet, consectetur adipisicing elit,<br><span class="more">More...</span></p>
    </div>
    <div class="abs service" style="left:459px;top:156px">
      <div class="abs icon" role="img" aria-label="Delivery truck icon"></div>
      <h3 class="abs">Delivery</h3>
      <p class="abs">Lorem ipsum dolor sit amet, consectetur adipisicing elit,<br><span class="more">More...</span></p>
    </div>
    <div class="abs service" style="left:775px;top:156px">
      <div class="abs icon" role="img" aria-label="Catering icon"></div>
      <h3 class="abs">Catering</h3>
      <p class="abs">Lorem ipsum dolor sit amet, consectetur adipisicing elit,<br><span class="more">More...</span></p>
    </div>
  </section>

  <div class="abs label" style="left:141px;top:982px;width:256px">Our Menus</div>
  <div class="abs menu-col" style="left:141px;top:1018px;width:190px">
    <h4>Breakfast</h4>
    <p>Lorem ipsum dolor sit amet, consectetur adipisicing elit,</p>
  </div>
  <div class="abs menu-col" style="left:350px;top:1018px;width:190px">
    <h4>Lunch and Dinner</h4>
    <p>Duis aute irure dolor in repre henderit in voluptate velit.</p>
  </div>
  <div class="abs track"><span class="start"></span><span class="grip"></span></div>

  <div class="abs divider"></div>

  <div class="abs label" style="left:642px;top:982px;width:152px">Contact Information</div>
  <div class="abs contact" style="left:642px;top:1023px;width:190px">
    <p>0109 / D4 Duis aute irure<br>dolor in repre ....</p>
    <p class="mail">info@thimbledeli-mail.com</p>
    <p class="copy">© 2012 | Privacy policy</p>
  </div>

  <svg class="abs" style="left:890px;top:982px" width="44" height="26" viewBox="0 0 44 26" aria-hidden="true">
    <path d="M4 6 Q26 0 30 18" fill="none" stroke="#222" stroke-width="4"/>
    <path d="M22 14 L30 24 L38 14 Z" fill="#222"/>
  </svg>
  <div class="abs order-btn">Order Now!</div>
  <div class="abs world" role="img" aria-label="Grey world map"></div>

  <footer class="abs footer">
    <div class="abs foot-nav">
      <a class="active" href="#">Home</a><a href="#">Menus</a><a href="#">Gallery</a><a href="#">About Us</a><a href="#">Media &amp; Events</a><a href="#">Hours &amp; Location</a><a href="#">Order Online</a><a href="#">Contact Us</a>
    </div>
    <div class="abs social"><span></span><span></span><span></span><span></span></div>
  </footer>
</div>
</body>
</html>
```